Global Expert Network Firm needs business card design

We need business card design for a new company based in Seoul, South Korea called 'Corwell Insight Partners'. We recruit industry experts covering all countries and connect our client and recruited expert by phone, face-to-face meetings and etc. We are a global expert network firm that is focused on delivering high-quality experts to our clients throughout the world. Our clients include multinational corporations, global consulting firms, private equity firms, venture capital firms, asset management companies.
We have made new logo and please find attachment.(Please use new logo)
Target Market(s)
Global Consulting Firms, Investment Firms, Private Equity Firms, Venture Capital Firms.
Industry/Entity Type
Recruitment
Contact Information for Business Card
We need two Languages (English and Korean Version).
The front is Korean and the back is English version.
[The back] [English]
Company Name: Corwell Insight Partners, Inc.
CEO Name: Daniel Park
Address: #507, Hanbit Bldg, 82 Maebongsan-ro, Dobong-gu, Seoul, 01327, Korea
Tel. +82 2 718 4052
Fax. +82 2 864 1097
Mobile. +82 10 7264 8815
Email: daniel@corwellip.com
Web: www.corwellip.com
[The front] [Korean] => Described in same order as English version.
회사명: 코웰인사이트파트너스(주)
대표이사: 박도현
주소: 서울시 도봉구 매봉산로 82 한빛빌딩 507호
Tel. 02 718 4052
Fax. 02 864 1097
Mobile. 010 7264 8815
Web: www.corwellip.com
Look and feel
Each slider illustrates characteristics of the customer's brand and the style your logo design should communicate.

```html
<!DOCTYPE html>
<html lang="ko">
<head>
<meta charset="utf-8">
<title>Corwell Insight Partners — Business Card</title>
<link rel="stylesheet" href="https://fonts.googleapis.com/css2?family=Lato:wght@400;700&family=Noto+Sans+KR:wght@400;500;700&display=swap">
<style>
  :root {
    --navy: #1c2354;
    --charcoal: #323133;
    --white: #ffffff;
    --ink: #2b2b2d;
    --backdrop: #e7eaee;
  }
  * { margin: 0; padding: 0; box-sizing: border-box; }
  html, body { width: 1200px; height: 1200px; overflow: hidden; }
  body {
    background: var(--backdrop);
    font-family: "Lato", "Noto Sans KR", sans-serif;
    position: relative;
  }
  .card {
    position: absolute;
    left: 191px;
    width: 817px;
    overflow: hidden;
  }
  .card--english { top: 44px; height: 490px; }
  .card--korean { top: 634px; height: 492px; }
  .band { position: absolute; left: 0; width: 100%; }
  .band--navy { background: var(--navy); }
  .band--charcoal { background: var(--charcoal); }
  .band--white { background: var(--white); }

  .wordmark {
    position: absolute;
    color: var(--white);
    font-family: "Lato", sans-serif;
    font-weight: 400;
    text-transform: uppercase;
    letter-spacing: 0.02em;
    line-height: 1;
  }
  .wordmark span { display: block; }

  .card--english .wordmark { left: 86px; top: 86px; font-size: 32px; }
  .card--english .wordmark span + span { margin-top: 24px; }

  .mobile-line {
    position: absolute;
    display: flex; align-items: center; gap: 8px;
    font-size: 16px; color: var(--ink);
  }
  .icon { width: 20px; height: 20px; flex: none; }

  .person-name {
    position: absolute;
    right: 60px; top: 300px;
    font-size: 31px; color: var(--ink);
    line-height: 1;
  }
  .person-name strong { font-weight: 700; letter-spacing: 0.01em; }
  .person-name em { font-style: normal; font-weight: 400; }

  .contact-col {
    position: absolute;
    color: var(--white);
    font-size: 16px;
    line-height: 21px;
  }
  .contact-col .icon { display: block; margin-bottom: 6px; }

  .logo-block {
    position: absolute;
    left: 290px; top: 55px;
    width: 239px; height: 239px;
    background: var(--navy);
  }
  .card--korean .wordmark { left: 11px; top: 40px; font-size: 30px; }
  .card--korean .wordmark span + span { margin-top: 34px; }

  .ceo {
    position: absolute;
    left: 600px; top: 56px;
    width: 145px;
    text-align: center;
    color: var(--white);
    font-family: "Noto Sans KR", sans-serif;
  }
  .ceo__title { font-size: 20px; font-weight: 400; letter-spacing: 0.12em; }
  .ceo__name { font-size: 31px; font-weight: 700; letter-spacing: 0.08em; margin-top: 2px; }

  .card--korean .mobile-line { left: 590px; top: 152px; color: var(--white); font-size: 16px; }

  .company-line {
    position: absolute;
    left: 0; width: 100%; top: 305px;
    text-align: center;
    font-family: "Noto Sans KR", sans-serif;
    font-size: 27px;
    color: var(--ink);
    line-height: 36px;
  }
  .company-line__label { font-size: 22px; letter-spacing: 0.12em; }
  .company-line__value { letter-spacing: 0.06em; }

  .card--korean .contact-col { font-family: "Lato", "Noto Sans KR", sans-serif; }
</style>
</head>
<body>

<!-- English side -->
<section class="card card--english" aria-label="Business card, English side">
  <div class="band band--navy" style="top:0;height:293px"></div>
  <div class="band band--white" style="top:293px;height:52px"></div>
  <div class="band band--charcoal" style="top:345px;height:145px"></div>

  <div class="wordmark" aria-label="Corwell Insight Partners">
    <span>Corwell</span><span>Insight</span><span>Partners</span>
  </div>

  <div class="mobile-line" style="left:76px;top:308px">
    <svg class="icon" viewBox="0 0 20 20" aria-hidden="true"><rect x="5" y="1.5" width="10" height="17" rx="1.5" fill="none" stroke="currentColor" stroke-width="1.8"/><line x1="8.5" y1="15.5" x2="11.5" y2="15.5" stroke="currentColor" stroke-width="1.6"/></svg>
    <span>+82 10 7264 8815</span>
  </div>

  <div class="person-name"><strong>DANIEL</strong> <em>Park</em></div>

  <div class="contact-col" style="left:76px;top:372px">
    <svg class="icon" viewBox="0 0 20 20" aria-hidden="true"><path d="M10 2 L19 10 H16 V18 H12 V13 H8 V18 H4 V10 H1 Z" fill="currentColor"/></svg>
    #507, Hanbit Bldg, 82 Maebongsan-ro,<br>Dobong-gu, Seoul, 01327, Korea
  </div>
  <div class="contact-col" style="left:404px;top:372px">
    <svg class="icon" viewBox="0 0 20 20" aria-hidden="true"><path d="M2 7 Q10 1 18 7 L16 9 L13 8 V6.5 Q10 5.5 7 6.5 V8 L4 9 Z" fill="currentColor"/><path d="M5 10 H15 L17 17 H3 Z" fill="currentColor"/><circle cx="10" cy="13.5" r="2" fill="var(--charcoal)"/></svg>
    Tel. +82 2 718 4052<br>Fax. +82 2 864 1097
  </div>
  <div class="contact-col" style="left:596px;top:372px">
    <svg class="icon" viewBox="0 0 20 20" aria-hidden="true"><rect x="1.5" y="2.5" width="17" height="11" fill="none" stroke="currentColor" stroke-width="2"/><rect x="8" y="13.5" width="4" height="3" fill="currentColor"/><rect x="5" y="16.5" width="10" height="1.8" fill="currentColor"/></svg>
    daniel@corwellip.com<br>www.corwellip.com
  </div>
</section>

<!-- Korean side -->
<section class="card card--korean" aria-label="Business card, Korean side">
  <div class="band band--charcoal" style="top:0;height:294px"></div>
  <div class="band band--white" style="top:294px;height:52px"></div>
  <div class="band band--navy" style="top:346px;height:146px"></div>

  <div class="logo-block">
    <div class="wordmark" aria-label="Corwell Insight Partners">
      <span>Corwell</span><span>Insight</span><span>Partners</span>
    </div>
  </div>

  <div class="ceo">
    <div class="ceo__title">대표이사:</div>
    <div class="ceo__name">박도현</div>
  </div>

  <div class="mobile-line">
    <svg class="icon" viewBox="0 0 20 20" aria-hidden="true"><rect x="5" y="1.5" width="10" height="17" rx="1.5" fill="none" stroke="currentColor" stroke-width="1.8"/><line x1="8.5" y1="15.5" x2="11.5" y2="15.5" stroke="currentColor" stroke-width="1.6"/></svg>
    <span>010 7264 8815</span>
  </div>

  <div class="company-line">
    <span class="company-line__label">회사명:</span>
    <span class="company-line__value">코웰인사이트파트너스(주)</span>
  </div>

  <div class="contact-col" style="left:60px;top:374px">
    <svg class="icon" viewBox="0 0 20 20" aria-hidden="true"><path d="M10 2 L19 10 H16 V18 H12 V13 H8 V18 H4 V10 H1 Z" fill="currentColor"/></svg>
    주소: 서울시 도봉구 매봉산로 82<br>한빛빌딩 507호
  </div>
  <div class="contact-col" style="left:396px;top:374px">
    <svg class="icon" viewBox="0 0 20 20" aria-hidden="true"><path d="M2 7 Q10 1 18 7 L16 9 L13 8 V6.5 Q10 5.5 7 6.5 V8 L4 9 Z" fill="currentColor"/><path d="M5 10 H15 L17 17 H3 Z" fill="currentColor"/><circle cx="10" cy="13.5" r="2" fill="var(--navy)"/></svg>
    Tel. 02 718 4052<br>Fax. 02 864 1097
  </div>
  <div class="contact-col" style="left:588px;top:374px">
    <svg class="icon" viewBox="0 0 20 20" aria-hidden="true"><rect x="1.5" y="2.5" width="17" height="11" fill="none" stroke="currentColor" stroke-width="2"/><rect x="8" y="13.5" width="4" height="3" fill="currentColor"/><rect x="5" y="16.5" width="10" height="1.8" fill="currentColor"/></svg>
    daniel@corwellip.com<br>www.corwellip.com
  </div>
</section>

</body>
</html>
```